Dean Hollis Business Card

In addition to my name design (file uploaded), black print on white card stock, e-mail address should be presented as a typical e-mail address, i.e., underlined and in blue ink, the card should include the following information:
Instructor of Aerospace Systems
Aircraft Incident Review Consultant
Senior Certified Multi-Engine Pilot

dhollis@vexmail.example
Ridgefall, Montana
(907) 318-5074

```html
<!DOCTYPE html>
<html lang="en">
<head>
<meta charset="utf-8">
<title>Dean Hollis – Business Card</title>
<link rel="stylesheet" href="https://fonts.googleapis.com/css2?family=Oswald:wght@600&family=Arimo:wght@400&display=swap">
<style>
  :root {
    --paper: #ededed;
    --ink: #1c1c1c;
    --royal-top: #0a2f9e;
    --royal-bottom: #1f78ec;
    --sky: #45bdf0;
    --navy-text: #0c2a8c;
    --white: #ffffff;
  }
  html, body { margin: 0; padding: 0; overflow: hidden; background: var(--white); }
  .card {
    position: relative;
    width: 1200px;
    height: 720px;
    overflow: hidden;
    background: var(--paper);
    font-family: "Arimo", Arial, sans-serif;
  }
  .front, .back {
    position: absolute;
    top: 0;
    height: 720px;
    background: linear-gradient(160deg, #f2f2f2, #e6e6e6);
  }
  .front { left: 0; width: 728px; }
  .back { left: 728px; width: 472px; border-left: 1px solid #d0d0d0; box-sizing: border-box; }
  .wave { position: absolute; inset: 0; width: 100%; height: 100%; }
  .name {
    position: absolute;
    left: 94px;
    top: 142px;
    margin: 0;
    font-family: "Oswald", "Arial Narrow", sans-serif;
    font-weight: 600;
    font-size: 104px;
    line-height: 1;
    letter-spacing: 4px;
    color: var(--ink);
    text-transform: uppercase;
  }
  .contact {
    position: absolute;
    left: 80px;
    top: 460px;
    margin: 0;
    padding: 0;
    list-style: none;
    color: var(--white);
    font-size: 33px;
  }
  .contact li {
    display: flex;
    align-items: center;
    height: 46px;
    margin-bottom: 20px;
  }
  .contact svg { width: 44px; height: 36px; margin-right: 20px; flex: none; }
  .contact a { color: var(--white); text-decoration: none; }
  .roles {
    position: absolute;
    left: 3px;
    top: 458px;
    margin: 0;
    padding: 0;
    list-style: none;
    color: var(--navy-text);
    font-size: 25.5px;
  }
  .roles li { height: 37px; margin-bottom: 37px; white-space: nowrap; }
</style>
</head>
<body>
<div class="card">
  <section class="front">
    <svg class="wave" viewBox="0 0 728 720" preserveAspectRatio="none" aria-hidden="true">
      <defs>
        <linearGradient id="royal-front" x1="0" y1="0" x2="0" y2="1">
          <stop offset="0" stop-color="var(--royal-top)"/>
          <stop offset="1" stop-color="var(--royal-bottom)"/>
        </linearGradient>
      </defs>
      <path d="M0,338 C170,420 470,440 728,318 L728,720 L0,720 Z" fill="var(--sky)"/>
      <path d="M0,366 C200,446 490,438 728,330 L728,720 L0,720 Z" fill="url(#royal-front)"/>
    </svg>
    <h1 class="name">Dean Hollis</h1>
    <ul class="contact">
      <li>
        <svg viewBox="0 0 44 36" aria-hidden="true">
          <path d="M14,3 C10,4 8,8 9,14 C10,22 15,30 21,33 C24,34 26,33 27,31 L23,26 C22,25 21,25 20,26 C17,23 15,18 15,14 C16,13 17,13 17,11 L16,4 Z" fill="var(--white)"/>
        </svg>
        <span>(907) 318-5074</span>
      </li>
      <li>
        <svg viewBox="0 0 44 36" aria-hidden="true">
          <rect x="2" y="6" width="40" height="26" fill="var(--white)"/>
          <path d="M2,6 L22,21 L42,6" fill="none" stroke="var(--royal-top)" stroke-width="2"/>
        </svg>
        <a href="mailto:dhollis@vexmail.example">dhollis@vexmail.example</a>
      </li>
      <li>
        <svg viewBox="0 0 44 36" aria-hidden="true">
          <path d="M22,2 L42,19 L37,19 L37,35 L27,35 L27,24 L17,24 L17,35 L7,35 L7,19 L2,19 Z" fill="var(--white)"/>
        </svg>
        <span>Ridgefall, Montana</span>
      </li>
    </ul>
  </section>
  <section class="back">
    <svg class="wave" viewBox="0 0 472 720" preserveAspectRatio="none" aria-hidden="true">
      <defs>
        <linearGradient id="royal-back" x1="0" y1="0" x2="0" y2="1">
          <stop offset="0" stop-color="var(--royal-bottom)"/>
          <stop offset="1" stop-color="var(--royal-top)"/>
        </linearGradient>
      </defs>
      <path d="M0,0 H472 V262 C330,256 150,282 0,334 Z" fill="var(--sky)"/>
      <path d="M0,0 H472 V230 C320,234 150,266 0,322 Z" fill="url(#royal-back)"/>
    </svg>
    <ul class="roles">
      <li>Instructor of Aerospace Systems</li>
      <li>Aircraft Incident Review Consultant</li>
      <li>Senior Certified Multi-Engine Pilot</li>
    </ul>
  </section>
</div>
</body>
</html>
```